Retractable Banner Design for Retail Shopping Event

I need a design for a 33” by 86” retractable banner. It should have my logo at the top (the largest element of the design) and the banner should also include my website and Instagram handle:
www.mirabelhtx.com
@mirabelhtx
I have included product pictures in the brief that can be used. I also included different versions of my logo file, including AI. I need the file to be ready to upload to my printer.
My store is an upscale women’s boutique. I am also attaching designs I have selected in the past to give an idea of my aesthetic.

```html
<!DOCTYPE html>
<html lang="en">
<head>
<meta charset="utf-8">
<title>Mirabel HTX – Our Collections</title>
<link rel="stylesheet" href="https://fonts.googleapis.com/css2?family=Tenor+Sans&family=Libre+Baskerville&display=swap">
<style>
  :root{
    --ink:#5d5e60;
    --ink-dark:#2b2b2b;
    --rule:#8a8a8c;
    --blush:#efd2cb;
    --mist:#edecee;
    --gold-deep:#b8902f;
    --gold-light:#f0c65f;
    --gold-pale:#e9d9a8;
    --white:#ffffff;
  }
  *{box-sizing:border-box;margin:0;padding:0}
  html,body{width:1200px;height:3127px;overflow:hidden}
  body{
    position:relative;
    font-family:"Tenor Sans",sans-serif;
    color:var(--ink);
    background:linear-gradient(180deg,var(--blush) 0%,var(--mist) 48%,var(--mist) 55%,var(--blush) 100%);
  }
  .brand{
    position:absolute;left:0;top:130px;width:1200px;text-align:center;color:var(--ink);
    font-family:"Tenor Sans",sans-serif;line-height:1;white-space:nowrap;
  }
  .brand-name{display:block;font-size:150px;letter-spacing:2px}
  .brand-city{display:block;font-size:50px;letter-spacing:8px;margin-top:56px}

  .section-title{
    position:absolute;left:228px;top:427px;width:743px;height:127px;
  }
  .section-title .rule{position:absolute;background:var(--ink)}
  .rule.top{left:0;top:0;width:601px;height:4px}
  .rule.left{left:0;top:0;width:4px;height:113px}
  .rule.bottom{left:138px;bottom:0;width:605px;height:4px}
  .rule.right{right:0;bottom:0;width:4px;height:111px}
  .section-title h1{
    position:absolute;left:0;right:0;top:22px;text-align:center;white-space:nowrap;
    font-weight:400;font-size:72px;letter-spacing:-2px;color:var(--ink);line-height:1;
  }

  .card{
    position:absolute;left:305px;width:582px;height:556px;border-radius:30px;
    border:16px solid var(--gold-pale);
    background:rgba(255,255,255,.55);
  }
  .card-frame{
    position:absolute;left:17px;top:17px;right:17px;bottom:17px;
    background:linear-gradient(90deg,var(--gold-deep),var(--gold-light) 30%,var(--gold-deep) 55%,var(--gold-light) 80%,var(--gold-deep));
    padding:14px;border-radius:4px;
  }
  .card-face{width:100%;height:100%;background:var(--white)}
  .card-rule{
    position:absolute;left:63px;top:58px;width:424px;height:391px;
    border:4px solid var(--rule);
  }
  .card-label{
    position:absolute;left:50%;bottom:0;transform:translate(-50%,52%);
    background:var(--white);padding:0 8px;white-space:nowrap;
    font-size:66px;line-height:1.1;color:var(--ink);
  }
  .product{position:absolute}
  .product-jewelry{left:52px;top:121px;width:316px;height:152px;border-radius:40px;
    background:radial-gradient(circle at 25% 50%,#e8c25a 0 22%,transparent 36%),radial-gradient(circle at 75% 50%,#e8c25a 0 22%,transparent 36%)}
  .product-tray{left:41px;top:70px;width:346px;height:236px;border-radius:50%;
    background:radial-gradient(ellipse,#d9b878 0%,#b89356 60%,#8a6a3a 100%)}
  .product-slippers{left:44px;top:61px;width:336px;height:275px;border-radius:40%;
    background:linear-gradient(160deg,#eedfd3 0%,#d8c4bc 45%,#9a8ea0 100%)}
  .product-tote{left:86px;top:27px;width:251px;height:291px;border-radius:8px 8px 4px 4px;
    background:linear-gradient(180deg,#e9d8cf 0%,#dcc6bb 100%)}

  .footer{
    position:absolute;left:0;top:3021px;width:1200px;height:106px;background:var(--white);
    font-family:"Libre Baskerville",serif;font-size:44px;color:var(--ink-dark);white-space:nowrap;
  }
  .footer-web{position:absolute;left:36px;top:30px;display:flex;align-items:center;gap:10px;line-height:1}
  .footer-social{position:absolute;right:46px;top:26px;display:flex;align-items:center;gap:14px;line-height:1}
  .dot{width:42px;height:42px;border-radius:50%;background:var(--ink-dark)}
</style>
</head>
<body>
  <header class="brand">
    <span class="brand-name">MIRABEL</span>
    <span class="brand-city">HTX</span>
  </header>

  <div class="section-title">
    <span class="rule top"></span><span class="rule left"></span>
    <span class="rule bottom"></span><span class="rule right"></span>
    <h1>OUR COLLECTIONS</h1>
  </div>

  <section class="card" style="top:636px">
    <div class="card-frame"><div class="card-face"></div></div>
    <div class="card-rule">
      <div class="product product-jewelry" role="img" aria-label="Pair of gold quatrefoil stud earrings set with crystals"></div>
      <span class="card-label">jewelry</span>
    </div>
  </section>

  <section class="card" style="top:1234px">
    <div class="card-frame"><div class="card-face"></div></div>
    <div class="card-rule">
      <div class="product product-tray" role="img" aria-label="Round leopard print serving tray"></div>
      <span class="card-label">The Home</span>
    </div>
  </section>

  <section class="card" style="top:1817px">
    <div class="card-frame"><div class="card-face"></div></div>
    <div class="card-rule">
      <div class="product product-slippers" role="img" aria-label="Lavender slide slippers with blush pom-pom straps"></div>
      <span class="card-label">Sleep</span>
    </div>
  </section>

  <section class="card" style="top:2408px">
    <div class="card-frame"><div class="card-face"></div></div>
    <div class="card-rule">
      <div class="product product-tote" role="img" aria-label="Blush leather tote bag with a teal snake print"></div>
      <span class="card-label">Accessories</span>
    </div>
  </section>

  <footer class="footer">
    <div class="footer-web">
      <svg width="46" height="46" viewBox="0 0 46 46" fill="none" stroke="#2b2b2b" stroke-width="4">
        <circle cx="23" cy="23" r="20"/>
        <ellipse cx="23" cy="23" rx="9" ry="20"/>
        <line x1="3" y1="23" x2="43" y2="23"/>
        <path d="M7 12h32M7 34h32"/>
      </svg>
      <span>www.mirabelhtx.com</span>
    </div>
    <div class="footer-social">
      <span class="dot"></span>
      <span>@mirabelhtx</span>
    </div>
  </footer>
</body>
</html>
```